Visual design for database driven web application

Need a clean, professional looking visual design for a web application.

PLUME is the new standardized K-12 school testing program for the state of Texas. We are building an application named PLUME-Finder (clever, yeah?) that will allow teachers, school administrators, and others to EASILY sort through millions of records of student data and print or export reports showing just the information they need about their students.

The state currently doesn't provide a user-friendly way to do this. They provide a "data dump" spreadsheet that school administrators and teachers must figure out how to manipulate to get the data they need. We are building a Web-based tool that will make it super simple and easy for our users to get the data they need in a format that works for them.

I've created a basic wireframe of the main application screen in Vellum QD Max. I need you to "skin" the wireframe to make it look good. Your mockup will set the tone for branding and visual design throughout the site.

See the attached screenshots. There are a few variations of the screen that include dynamic panels that open & close. Start by designing just the main screen and if you have time, do one or two of the panels. Thanks!
Updates

Target Market(s)

K-12 education professionals (teachers, administrators) in the state of Texas

Industry/Entity Type

Building

Requirements
Must have
• Your mockups should include all of the features & content shown in the attached screenshots.

However, you don't have to show all 10 rows of data. You can just do the column headers and one row of data. (It would be repetitive and unnecessary to spend time re-creating the entire grid with all of that data just to show your visual styling.)

The design should reflect the following concepts:

- Texas
- Education
- Simplicity
- Helpfulness
- Trust
- Professionalism

If I select your design, I will want your design source files (Illustrator, Photoshop, etc.)
Nice to have
• A logo in the upper left corner for PLUME-Finder. The logo should definitely communicate the design concepts described under "must have."

```html
<!DOCTYPE html>
<html lang="en">
<head>
<meta charset="utf-8">
<title>PLUME-Finder · Student Data</title>
<link rel="stylesheet" href="https://fonts.googleapis.com/css2?family=Arimo:wght@400;700&family=Open+Sans:wght@400;600;700&display=swap">
<style>
:root{
  --night:#0f1a4a;
  --night-deep:#0a123a;
  --sky:#22346f;
  --red:#d62a27;
  --red-dark:#a81c1a;
  --white:#ffffff;
  --yellow:#f4e13a;
  --ink:#1a1a1a;
  --link:#1b2fd0;
  --grid:#b9b9b9;
  --grey-box:#555d77;
}
*{box-sizing:border-box;margin:0;padding:0}
html,body{width:1200px;height:734px;overflow:hidden;background:var(--white)}
body{position:relative;font-family:"Arimo",Arial,sans-serif;color:var(--ink)}

.masthead{position:absolute;left:0;top:0;width:1200px;height:128px;
  background:radial-gradient(ellipse 260px 120px at 640px 95px,#c9c56a 0%,#5a6a7a 35%,transparent 70%),
             linear-gradient(180deg,#1a2360 0%,var(--sky) 70%,#2b3f7e 100%)}
.brand{position:absolute;left:30px;top:28px;font-family:"Open Sans",sans-serif;font-weight:700;
  font-size:64px;letter-spacing:-1px;color:var(--yellow);line-height:1}
.crowd{position:absolute;left:520px;top:10px;width:210px;height:92px;
  background:linear-gradient(180deg,#232323 0%,#0b0b0b 100%);border-radius:40px 40px 4px 4px;opacity:.9}
.welcome{position:absolute;left:763px;top:15px;width:414px;height:36px;background:var(--night-deep);
  border:2px solid #5a6588;font-family:"Open Sans",sans-serif;font-size:18px;display:flex;align-items:center;padding:0 8px}
.welcome .greet{color:var(--yellow);font-weight:600}
.welcome .account{margin-left:auto;color:var(--white);word-spacing:4px}
.quick-search{position:absolute;left:764px;top:88px;width:204px;height:30px;background:var(--grey-box);
  border:2px solid #2a3152;color:#b8bccb;font-family:"Open Sans",sans-serif;font-size:18px;padding:1px 8px}
.search-button{position:absolute;left:968px;top:88px;width:64px;height:30px;background:#6a7190;border:2px solid #2a3152}
.scope{position:absolute;left:972px;top:66px;width:62px;height:58px;background:linear-gradient(135deg,#cfd2db,#4b5068);opacity:.8;border-radius:6px}
.search-options{position:absolute;left:1041px;top:98px;color:var(--white);font-family:"Open Sans",sans-serif;font-size:18px}

.ribbon{position:absolute;left:0;top:124px;width:1200px;height:48px}
.nav-tab{position:absolute;top:138px;height:30px;font-family:"Open Sans",sans-serif;font-size:18px;
  color:var(--white);line-height:30px;text-align:center}
.nav-tab.current{color:var(--ink)}
.feed{position:absolute;left:476px;top:142px;color:var(--white);font-family:"Open Sans",sans-serif;font-size:18px;letter-spacing:.4px}
.clock{position:absolute;left:1008px;top:146px;color:var(--white);font-family:"Open Sans",sans-serif;font-size:13px}

.toolbar{position:absolute;top:192px;font-size:12px}
.toolbar a{color:var(--link)}
.small-links{position:absolute;left:805px;top:185px;font-size:10px}
.small-links a{color:var(--link)}
.small-links .sep{color:#aaa;margin:0 14px}
.pager{position:absolute;left:18px;font-size:12px;display:flex;align-items:center}
.pager a{color:var(--link)}
.pager .page{margin-left:30px}
.pager .page b{display:inline-block;background:#ddd;padding:1px 4px;font-weight:400}
.pager .next{margin-left:34px}
.pager .show{margin-left:63px}
.rows-select{display:inline-block;margin:0 10px 0 8px;width:49px;height:20px;border:1px solid #777;border-radius:4px;
  background:linear-gradient(#fff,#ddd);font-size:12px;padding-left:8px;line-height:18px;position:relative;vertical-align:middle}
.rows-select::after{content:"";position:absolute;right:0;top:0;width:16px;height:18px;background:#3b7be0;border-radius:0 3px 3px 0}

.grid-wrap{position:absolute;left:7px;top:278px;width:1193px;height:365px;overflow:hidden;border-left:2px solid #888}
.grid{border-collapse:collapse;table-layout:fixed;width:1250px;font-size:12px}
.grid col{width:95.6px}
.grid th{text-align:left;font-weight:700;height:18px;padding:0 2px;border:1px solid var(--grid);border-bottom:2px solid #999}
.grid td{vertical-align:top;height:34.5px;padding:1px 2px;border:1px solid var(--grid);line-height:15px;overflow-wrap:anywhere}

.footer{position:absolute;left:0;top:700px;width:1180px;height:34px;background:var(--night);
  color:var(--yellow);font-size:10px}
.footer span{position:absolute;top:11px}
</style>
</head>
<body>
<header class="masthead">
  <div class="brand">PLUME-Finder</div>
  <div class="crowd" role="img" aria-label="Silhouettes of cheering students against a glowing horizon"></div>
  <div class="welcome"><span class="greet">Welcome, Miles</span><span class="account">my profile / log out</span></div>
  <div class="quick-search">Quick Search</div>
  <div class="search-button"></div>
  <div class="scope" role="img" aria-label="Telescope search icon"></div>
  <div class="search-options">search options</div>
</header>

<svg class="ribbon" viewBox="0 0 1200 48" aria-hidden="true">
  <polygon points="22,2 1200,2 1200,12 30,14" fill="var(--red)"/>
  <rect x="0" y="13" width="1180" height="34" fill="var(--night)"/>
  <polygon points="33,17 111,17 118,45 40,45" fill="var(--red)" stroke="var(--red-dark)"/>
  <polygon points="116,17 248,17 255,45 123,45" fill="var(--red)" stroke="var(--red-dark)"/>
  <polygon points="254,17 406,17 413,45 261,45" fill="var(--white)" stroke="var(--red)" stroke-width="2"/>
</svg>
<nav>
  <div class="nav-tab" style="left:36px;width:78px">Home</div>
  <div class="nav-tab" style="left:126px;width:126px">Instructions</div>
  <div class="nav-tab current" style="left:262px;width:146px">Student Data</div>
</nav>
<div class="feed">&lt;&lt;&lt; Ideal location for an optional information feed. &lt;&lt;&lt;</div>
<div class="clock">11/30/2011 &nbsp;1:51 pm CST</div>

<main>
  <div class="toolbar" style="left:27px">Showing 26 of 38 columns</div>
  <div class="toolbar" style="left:189px"><a href="#">show / hide columns</a> &nbsp;<span style="color:#999">◀</span></div>
  <div class="toolbar" style="left:390px">3 columns are <a href="#">filtered</a>.</div>
  <div class="small-links"><a href="#">print</a><span class="sep">|</span><a href="#">download</a></div>

  <div class="pager" style="top:240px"><a href="#">Previous</a><span class="page">page 1 <b>2</b> 3 &nbsp;… &nbsp;47</span><a class="next" href="#">Next</a><span class="show">Show</span><span class="rows-select">10</span>rows per page</div>

  <div class="grid-wrap">
    <table class="grid">
      <colgroup><col><col><col><col><col><col><col><col><col><col><col><col><col></colgroup>
      <thead><tr><th>Date</th><th>Grade</th><th>ESC</th><th>CDC #</th><th>District</th><th>Campus</th><th>Last Name</th><th>First Name</th><th>MI</th><th>Student ID</th><th>Gender</th><th>DOB</th><th>Hisp</th></tr></thead>
      <tbody>
        <tr><td>411</td><td>9</td><td>10</td><td>999999001</td><td>EXAMPLE DISTRICT</td><td>EXAMPLE H S</td><td>ABERNATHYSMITH</td><td>NOELLE</td><td></td><td>611204875</td><td>F</td><td>6141996</td><td>1</td></tr>
        <tr><td>411</td><td>9</td><td>10</td><td>999999001</td><td>EXAMPLE DISTRICT</td><td>EXAMPLE H S</td><td>ACKERBLOMEN</td><td>HOLDEN</td><td></td><td>S12739018</td><td>M</td><td>8221996</td><td>1</td></tr>
        <tr><td>411</td><td>9</td><td>10</td><td>999999001</td><td>EXAMPLE DISTRICT</td><td>EXAMPLE H S</td><td>AINSLEY</td><td>CORBIN</td><td>T</td><td>S12950473</td><td>M</td><td>10141994</td><td>1</td></tr>
        <tr><td>411</td><td>9</td><td>10</td><td>999999001</td><td>EXAMPLE DISTRICT</td><td>EXAMPLE H S</td><td>ALDRIDGE</td><td>MAISIE</td><td>R</td><td>627413958</td><td>F</td><td>3091996</td><td>1</td></tr>
        <tr><td>411</td><td>9</td><td>10</td><td>999999001</td><td>EXAMPLE DISTRICT</td><td>EXAMPLE H S</td><td>ALLENDALE</td><td>JUNE</td><td></td><td>S12886120</td><td>F</td><td>6231996</td><td>0</td></tr>
        <tr><td>411</td><td>9</td><td>10</td><td>999999001</td><td>EXAMPLE DISTRICT</td><td>EXAMPLE H S</td><td>ALMSWORTH</td><td>TARIQ</td><td>D</td><td>347815602</td><td>M</td><td>2141996</td><td>0</td></tr>
        <tr><td>411</td><td>9</td><td>10</td><td>999999001</td><td>EXAMPLE DISTRICT</td><td>EXAMPLE H S</td><td>ALTAMIRA</td><td>ILIANA</td><td>C</td><td>651037284</td><td>F</td><td>7081997</td><td>1</td></tr>
        <tr><td>411</td><td>9</td><td>10</td><td>999999001</td><td>EXAMPLE DISTRICT</td><td>EXAMPLE H S</td><td>ALTMAN</td><td>REID</td><td>K</td><td>618274590</td><td>M</td><td>8191994</td><td>1</td></tr>
        <tr><td>411</td><td>9</td><td>10</td><td>999999001</td><td>EXAMPLE DISTRICT</td><td>EXAMPLE H S</td><td>ALTAMIRAN</td><td>ROLAND</td><td>P</td><td>S12791346</td><td>M</td><td>5121994</td><td>1</td></tr>
        <tr><td>411</td><td>9</td><td>10</td><td>999999001</td><td>EXAMPLE DISTRICT</td><td>EXAMPLE H S</td><td>ALTHAUSER</td><td>RAMIRO</td><td></td><td>624961738</td><td>M</td><td>2261996</td><td>1</td></tr>
      </tbody>
    </table>
  </div>

  <div class="pager" style="top:660px"><a href="#">Previous</a><span class="page">page 1 <b>2</b> 3 &nbsp;… &nbsp;47</span><a class="next" href="#">Next</a><span class="show">Show</span><span class="rows-select">10</span>rows per page</div>
</main>

<footer class="footer">
  <span style="left:428px">Copyright © 2012 &nbsp;PLUME-Finder</span>
  <span style="left:627px">Terms of Use &nbsp;/ &nbsp;Privacy Policy &nbsp;/ &nbsp;Contact Us</span>
</footer>
</body>
</html>
```